Lumivane, Business Intelligence Consultant Web Design

We need a web design for a Business Intelligence Consultant Enterprise.
We design, develop and mantain management systems and reports that delivered to the final user a complete information about their business. With that information they can take better management decisions.
Our principal service is KRV Business Intelligence proyects, using KRV Stockvault and KRV Quillmark tools.
Also we develop web systems that integrate mobile technology with KRV Systems and end user database systems.

Our principal objective is to be a partner of our clients more than a service provider, the idea is to offer a complete service to our customers that allow both companies grow togheter.

The final design must present our list of services and products, and show our experience in business intelligence projects.

Target Market(s)

Companies that runs KRV systems, Business companies, companies with production processes, retail, logistic process (inventory management)

Industry/Entity Type

Business

Requirements
Must have
• The brochure must have 4 pages:
Home
Empresa
Business Intelligence
Aplicaciones empresariales móviles
Metodología

And a contact form to receive customer contact.
- Name
- Company
- Contact Email
- Message text

For the color I will upload both company logos with different colors that u can use. Obviously you can add color if you want.
Nice to have
• The principal idea is to show to customer that all information of his business can be summarized on one graphic panel and can be consulted from any device.

Is nice to have business graphics on the web design, maybe abstract and give the idea of management information can be obtained easily.

Should not have
• Please, PLEASE!, don't use on the web site a meeting photo or people watching a business report on a lobby or some business man making a presentation.
Neither images of team building or people at the office.

That images are too used to present the business intelligence concept and the principal idea is to have information, and not people working hard to obtain that.

```html
<!DOCTYPE html>
<html lang="en">
<head>
<meta charset="utf-8">
<title>Lumivane — Business Intelligence</title>
<link rel="stylesheet" href="https://fonts.googleapis.com/css2?family=Arimo:wght@400;700&family=Source+Sans+3:wght@400;600&display=swap">
<style>
:root{
  --bar:#6d6d6d;
  --page:#e9e9e9;
  --panel:#ffffff;
  --red:#cc1f2b;
  --dark-red:#8e1a1e;
  --link:#c2502c;
  --text:#4a4a4a;
  --muted:#666;
  --nav-top:#4a4a4c;
  --nav-bottom:#1e1e20;
  --soft:#f4f4f4;
}
*{margin:0;padding:0;box-sizing:border-box}
html,body{width:1053px;height:1200px;overflow:hidden;background:var(--page)}
.site{position:relative;width:1000px;height:1140px;transform:scale(1.053);transform-origin:0 0;font-family:"Source Sans 3",sans-serif;color:var(--text)}
.abs{position:absolute}
.topbar{left:0;top:0;width:1000px;height:40px;background:var(--bar);border-bottom:2px solid #bdbdbd}
.toplinks{left:617px;top:13px;font-family:"Arimo",sans-serif;font-size:13px;color:#fff}
.toplinks span{margin:0 9px;color:#ddd}
.search{left:790px;top:6px;width:187px;height:24px;background:#fff;border:1px solid #ccc;border-radius:2px;font-family:"Arimo",sans-serif;font-size:11px;color:#aaa;padding:4px 13px}
.search svg{position:absolute;right:6px;top:6px}
.brand{left:27px;top:56px;display:flex;align-items:center;gap:14px}
.brand-mark{width:60px;height:60px;background:#8a8a8a}
.brand-name{font-family:"Source Sans 3",sans-serif;font-weight:600;font-size:54px;color:var(--red);letter-spacing:-1px;line-height:1}
.nav{left:426px;top:65px;width:557px;height:40px;display:flex;background:linear-gradient(var(--nav-top),var(--nav-bottom));border-radius:3px;box-shadow:0 1px 2px rgba(0,0,0,.4)}
.nav a{display:flex;align-items:center;justify-content:center;color:#eee;font-size:13.5px;text-decoration:none;border-right:1px solid #111;box-shadow:inset -1px 0 0 #555}
.nav a.active{background:linear-gradient(#d8343c,#a8141d);border-radius:3px 0 0 3px;color:#fff}
.panel{left:22px;top:136px;width:957px;height:857px;background:var(--panel);border-radius:3px;box-shadow:0 0 4px rgba(0,0,0,.18)}
.slider{left:39px;top:150px;width:922px;height:310px;border:1px solid #cfcfcf;background:#f5f5f5;box-shadow:0 2px 3px rgba(0,0,0,.15)}
.slide{left:51px;top:160px;width:898px;height:290px;background:#ececec;border:1px solid #d6d6d6}
.slide-art{left:60px;top:170px;width:372px;height:252px;background:radial-gradient(circle at 30% 35%,#4d8fd1 0,#b8c7d6 38%,#e2e2e2 70%);border-radius:4px}
.slide-copy{left:442px;top:240px;width:449px;font-size:17px;line-height:30px;color:#555;text-align:justify}
.arrow{top:287px;width:24px;height:35px;background:#fafafa;border:1px solid #ddd}
.dots{left:438px;top:424px;width:125px;height:24px;background:#f6f6f6;display:flex;justify-content:center;align-items:center;gap:6px;border-radius:3px 3px 0 0}
.dots i{width:12px;height:12px;border-radius:50%;background:#8a8a8a;box-shadow:inset 0 1px 2px rgba(0,0,0,.4)}
.dots i.on{background:var(--red)}
.slider-shadow{left:40px;top:460px;width:920px;height:45px;background:radial-gradient(ellipse at 50% 0,rgba(0,0,0,.12),rgba(0,0,0,0) 70%)}
.feature{top:522px;width:285px}
.feature-head{display:flex;align-items:center;gap:4px;height:36px}
.icon{width:35px;height:35px;border-radius:5px}
.feature h2,.block-title{font-family:"Arimo",sans-serif;font-weight:400;color:var(--red);font-size:20px}
.feature p{margin-top:17px;font-size:12.6px;line-height:18px;text-align:justify;color:#444}
.more{display:block;text-align:right;font-family:"Arimo",sans-serif;font-size:13px;color:var(--red);margin-top:4px}
.more b{font-weight:700;margin-left:3px}
.news{left:42px;top:704px;width:617px;height:226px;background:var(--soft)}
.news-head{left:4px;top:6px;display:flex;align-items:center;gap:8px}
.news-head .block-title{font-size:16px}
.news-item{left:9px;width:590px}
.news-item .meta{font-size:13px}
.news-item .meta a{color:var(--link);text-decoration:underline}
.news-item .meta span{font-size:11px;color:#333;margin-left:18px}
.news-item .meta span+span{margin-left:12px}
.news-item p{margin:14px 0 0 3px;font-size:10.6px;line-height:18px;color:#333}
.blog{left:677px;top:697px;width:293px;font-family:"Arimo",sans-serif}
.blog-head{display:flex;align-items:center;gap:10px}
.blog .date{font-size:12px;color:#555;margin-top:14px}
.blog p{font-size:11.4px;line-height:19px;color:#555;margin-top:17px;text-align:justify}
.footer{font-family:"Arimo",sans-serif}
.clients-title{left:47px;top:1014px;font-size:13px;color:var(--dark-red)}
.clients{left:44px;top:1045px;width:308px;height:62px;background:#fff;display:flex;align-items:center;justify-content:space-around;font-size:15px;color:#333}
.info{left:457px;top:1020px;font-size:13px;color:#111;line-height:14px}
.info h3{font-weight:400;color:var(--red);font-size:13.5px;margin-bottom:20px}
.social{left:829px;top:1018px;display:flex;gap:11px}
.social i{width:27px;height:27px;border-radius:3px;background:#3a6ea8}
.legal{right:32px;top:1070px;font-size:11px;color:#333}
.legal span{margin:0 8px}
.copy{right:30px;top:1100px;font-size:12.5px;color:#222}
</style>
</head>
<body>
<div class="site">
  <div class="abs topbar"></div>
  <div class="abs toplinks">Clients<span>|</span>Careers</div>
  <div class="abs search">Search
    <svg width="12" height="12" viewBox="0 0 12 12"><circle cx="5" cy="5" r="3.5" fill="none" stroke="#bbb" stroke-width="1.5"/><line x1="7.5" y1="7.5" x2="11" y2="11" stroke="#bbb" stroke-width="1.5"/></svg>
  </div>

  <div class="abs brand"><div class="brand-mark"></div><div class="brand-name">lumivane</div></div>

  <nav class="abs nav">
    <a class="active" style="width:66px">Home</a>
    <a style="width:95px">Empresa</a>
    <a style="width:162px">Business Intelligence</a>
    <a style="width:119px">Aplicaciones</a>
    <a style="width:115px;border:0;box-shadow:none">Metodología</a>
  </nav>

  <div class="abs panel"></div>
  <div class="abs slider"></div>
  <div class="abs slide"></div>
  <div class="abs slide-art" role="img" aria-label="Illustration of figures working at a laptop beside a blue globe"></div>
  <p class="abs slide-copy">Sed ut perspiciatis unde omnis iste natus error sit volupta-tem accusantium doloremque laudantium, totam rem aperiam, eaque ipsa quae ab illo inventore veritatis et quasi architecto</p>
  <div class="abs arrow" style="left:53px"><svg width="24" height="35" viewBox="0 0 24 35"><polyline points="14,12 9,17.5 14,23" fill="none" stroke="#bbb" stroke-width="1.5"/></svg></div>
  <div class="abs arrow" style="left:925px"><svg width="24" height="35" viewBox="0 0 24 35"><polyline points="10,12 15,17.5 10,23" fill="none" stroke="#bbb" stroke-width="1.5"/></svg></div>
  <div class="abs dots"><i></i><i></i><i class="on"></i><i></i><i></i><i></i></div>
  <div class="abs slider-shadow"></div>

  <section class="abs feature" style="left:48px">
    <div class="feature-head"><div class="icon" style="background:linear-gradient(#5aa8e0,#1f6aa8)"></div><h2>Our Services</h2></div>
    <p>Neque porro quisquam est, qui dolorem ipsum quia dolor sit amet, consectetur, adipisci velit, sed quia non numquam eius modi tempora incidunt ut labore et dolore magnam aliquam quaerat.</p>
    <a class="more">read more<b>»</b></a>
  </section>
  <section class="abs feature" style="left:369px;width:274px">
    <div class="feature-head"><div class="icon" style="background:linear-gradient(#4cbf4c,#1e7d26);margin-left:3px"></div><h2>Education &amp; Training</h2></div>
    <p>Neque porro quisquam est, qui dolorem ipsum quia dolor sit amet, consectetur, adipisci velit, sed quia non numquam eius modi tempora incidunt ut labore et dolore magnam aliquam quaerat.</p>
    <a class="more">read more<b>»</b></a>
  </section>
  <section class="abs feature" style="left:679px">
    <div class="feature-head"><div class="icon" style="background:linear-gradient(#52a6dc,#1d5f9a)"></div><h2>About Us</h2></div>
    <p>Neque porro quisquam est, qui dolorem ipsum quia dolor sit amet, consectetur, adipisci velit, sed quia non numquam eius modi tempora incidunt ut labore et dolore magnam aliquam quaerat.</p>
    <a class="more">read more<b>»</b></a>
  </section>

  <section class="abs news">
    <div class="abs news-head"><div class="icon" style="background:linear-gradient(#9a9a9a,#555)"></div><h2 class="block-title">Latest News</h2></div>
    <div class="abs news-item" style="top:48px">
      <div class="meta"><a>http://nortaleda.com/jdf5666/ jhb5/jj</a><span>May 17, 2012</span><span>9.30 Am</span></div>
      <p>Allam corporis suscipit laboriosam, nisi ut aliquid ex ea commodi consequatur Quis autem vel eum iure reprehenderit qui in No one rejects, dislikes, or avoids pleasure itself.</p>
    </div>
    <div class="abs news-item" style="top:141px">
      <div class="meta"><a>http://nortaleda.com/jdf5666/ jhb5/jj</a><span>May 17, 2012</span><span>9.30 Am</span></div>
      <p>Allam corporis suscipit laboriosam, nisi ut aliquid ex ea commodi consequatur Quis autem vel eum iure reprehenderit qui in No one rejects, dislikes, or avoids pleasure itself.</p>
    </div>
  </section>

  <section class="abs blog">
    <div class="blog-head" style="margin-left:6px"><div style="width:37px;height:27px;border-radius:4px;background:linear-gradient(#ffa040,#e65c10)"></div><h2 class="block-title">Blog</h2></div>
    <div class="date" style="margin-left:3px">May 17, 2012</div>
    <p style="margin-left:3px">Neque porro quisquam est, qui dolorem ipsum quia dolor sit amet, consectetur, adipisci velit, sed quia non numquam</p>
    <a class="more" style="margin-top:7px">read more <b>»</b></a>
    <div class="date">May 17, 2012</div>
    <p>Neque porro quisquam est, qui dolorem ipsum quia dolor sit amet, consectetur, adipisci velit, sed quia non numquam</p>
    <a class="more" style="margin-top:7px">read more <b>»</b></a>
  </section>

  <footer class="footer">
    <div class="abs clients-title">Our Clients</div>
    <div class="abs clients"><span>Harlow Trust</span><span>Ostrenza</span><span>Velcor</span></div>
    <div class="abs info">
      <h3>For more information:</h3>
      Loreum ipsum dollar,<br>Loreum ipsum dollar.<br><br>Phone : 555 014 2378<br>Email : info@lumivane.com
    </div>
    <div class="abs social" aria-label="Social links"><i></i><i></i><i></i><i></i></div>
    <div class="abs legal">Privacy Policy<span>|</span>Site Map</div>
    <div class="abs copy">© 2012 lumivane, All rights reserved</div>
  </footer>
</div>
</body>
</html>
```